Outdoor mass notification company needing business card design.

Our company name is Harborline Signal Systems Inc located in Amory Mississippi and we sell and maintain "Corvath" Mass Notification Sirens in the US. Outdoor sirens notify people of certain severe dangers such as tornados, severe thunderstorms, flooding, hurricanes and tsunamis. We also serve the oil and gas refining industries to warn of Chemical releases, fires, and lightning alerts.

Contact Information for Business Card

Name, title, cell number, email address

Requirements
Nice to have
• The Corvath logo and also the Tallbrook logo.

```html
<!DOCTYPE html>
<html lang="en">
<head>
<meta charset="utf-8">
<title>Harborline Signal Systems – Business Card</title>
<link href="https://fonts.googleapis.com/css2?family=Crimson+Text:wght@700&family=Poppins:wght@400&display=swap" rel="stylesheet">
<style>
  :root {
    --stage: #b7b7b7;
    --navy: #34536f;
    --paper: #ffffff;
    --divider: #9a9a9a;
    --rule: #8fa3b6;
    --siren-dark: #1d1f22;
    --siren-mid: #3a3d42;
    --pole: #55524e;
  }
  * { margin: 0; padding: 0; box-sizing: border-box; }
  html, body { width: 1200px; height: 1200px; overflow: hidden; }
  body { background: var(--stage); position: relative; font-family: "Poppins", sans-serif; }

  .card { position: absolute; top: 305px; height: 598px; overflow: hidden; }
  .card--front { left: 202px; width: 371px; background: var(--navy); }
  .card--back { left: 603px; width: 366px; background: var(--navy); }

  .product-photo { position: absolute; inset: 0; }
  .product-photo .siren {
    position: absolute; left: 97px; top: 8px; width: 178px; height: 398px;
    border-radius: 10px;
    background: linear-gradient(90deg, var(--siren-dark), var(--siren-mid) 50%, var(--siren-dark));
  }
  .product-photo .pole {
    position: absolute; left: 154px; top: 412px; width: 64px; bottom: 0;
    background: linear-gradient(90deg, #46443f, var(--pole) 50%, #46443f);
  }

  .wordmark {
    position: absolute; left: 0; right: 0; text-align: center;
    font-family: "Crimson Text", serif; font-weight: 700; line-height: 1;
    text-transform: uppercase;
  }
  .wordmark .line-1 { display: block; font-size: 36px; letter-spacing: 0.5px; }
  .wordmark .line-2 { display: block; font-size: 27px; margin-top: 4px; }
  .card--front .wordmark { top: 478px; color: var(--paper); }

  .back-top {
    position: absolute; left: 0; top: 0; width: 100%; height: 297px;
    background: var(--paper); border-bottom: 3px solid var(--divider);
  }
  .card--back .wordmark { top: 128px; color: var(--navy); }

  .contact { position: absolute; left: 0; right: 0; top: 338px; text-align: center; color: var(--paper); }
  .contact .name { font-family: "Crimson Text", serif; font-weight: 700; font-size: 25px; line-height: 1; text-transform: uppercase; }
  .contact .title { font-size: 15px; line-height: 1.3; margin-top: 2px; }

  .icon-row { display: flex; align-items: center; justify-content: center; gap: 4px; margin-top: 14px; }
  .icon-row .rule { width: 52px; height: 1px; background: var(--rule); margin: 0 4px; }
  .icon-row .icon {
    width: 25px; height: 25px; border-radius: 3px; background: var(--paper);
    display: flex; align-items: center; justify-content: center;
  }
  .details { font-size: 15.5px; line-height: 21px; margin-top: 9px; }
  .separator { width: 196px; height: 1px; background: var(--rule); margin: 16px auto 12px; }
  .address { font-size: 15.5px; line-height: 21px; }
</style>
</head>
<body>
  <section class="card card--front">
    <div class="product-photo" role="img" aria-label="Photograph of a stacked outdoor warning siren mounted on a steel pole">
      <div class="siren"></div>
      <div class="pole"></div>
    </div>
    <div class="wordmark">
      <span class="line-1">Harborline</span>
      <span class="line-2">Signal Systems</span>
    </div>
  </section>

  <section class="card card--back">
    <div class="back-top"></div>
    <div class="wordmark">
      <span class="line-1">Harborline</span>
      <span class="line-2">Signal Systems</span>
    </div>
    <div class="contact">
      <p class="name">Daniel Reeves</p>
      <p class="title">Managing Director</p>
      <div class="icon-row">
        <span class="rule"></span>
        <span class="icon">
          <svg width="16" height="16" viewBox="0 0 24 24" fill="var(--navy)"><path d="M6.6 10.8a15 15 0 0 0 6.6 6.6l2.2-2.2a1 1 0 0 1 1-.25 11.4 11.4 0 0 0 3.6.57 1 1 0 0 1 1 1V20a1 1 0 0 1-1 1A17 17 0 0 1 3 4a1 1 0 0 1 1-1h3.5a1 1 0 0 1 1 1c0 1.25.2 2.45.57 3.57a1 1 0 0 1-.25 1z"/></svg>
        </span>
        <span class="icon">
          <svg width="16" height="16" viewBox="0 0 24 24" fill="none" stroke="var(--navy)" stroke-width="2"><rect x="3" y="5" width="18" height="14"/><path d="M3 5l9 8 9-8M3 19l7-7M21 19l-7-7"/></svg>
        </span>
        <span class="icon">
          <svg width="16" height="16" viewBox="0 0 24 24" fill="none" stroke="var(--navy)" stroke-width="2"><circle cx="12" cy="12" r="9"/><path d="M3 12h18M12 3c3 3 3 15 0 18M12 3c-3 3-3 15 0 18"/></svg>
        </span>
        <span class="rule"></span>
      </div>
      <div class="details">
        <p>662-555-0148</p>
        <p>info@harborlinesignal.com</p>
        <p>www.harborlinesignal.com</p>
      </div>
      <div class="separator"></div>
      <div class="address">
        <p>421, Address line goes here</p>
        <p>45452,Country Name</p>
      </div>
    </div>
  </section>
</body>
</html>
```